Equity, Effectiveness and Efficiency in charitable food relief sector

I am undertaking my PhD in food policy in the charitable food relief sector, specifically investigating the factors (supply, demand and capacity) that affect the introduction of nutrition policy and in turn, affect the sector's ability to achieve equity, effectiveness and efficiency.

I need a graphic device that incorporates this central idea of Equity, Effectiveness and Efficiency, and how the factors of supply, demand and capacity interact. There are sub-factors within supply (1-6), demand (7-10) and capacity (11 - 15). All these details are shown in the attached figure (Basic figure_Eq Effec Effic and factors.jpg)

This figure (Basic figure_Eq Effec Effic and factors.jpg) contains all the information I need in a graphic but I need something that is more visually appealing, and that can link the ideas in a format other than a table. The final graphic will outline how the food relief sector balances the core objectives of equity, effectiveness and efficiency with the factors (and sub-factors) of supply, demand and capacity.

```html
<!DOCTYPE html>
<html lang="en">
<head>
<meta charset="utf-8">
<title>Equity, Effectiveness, Efficiency — Factors that affect the introduction of nutrition policy</title>
<link rel="stylesheet" href="https://fonts.googleapis.com/css2?family=Jost:wght@400;500;600;700&display=swap">
<style>
  :root {
    --sky: #a4d9f5;
    --navy: #0b5ea4;
    --ring: #0a9fe0;
    --halo: #1a63a6;
    --white: #ffffff;
  }
  html, body {
    margin: 0;
    padding: 0;
    width: 1200px;
    height: 800px;
    overflow: hidden;
    background: var(--sky);
    font-family: "Jost", "Futura", sans-serif;
  }
  .canvas {
    position: relative;
    width: 1200px;
    height: 800px;
  }
  .band {
    position: absolute;
    left: 0;
    width: 1200px;
    background: var(--navy);
    color: var(--sky);
    display: flex;
    align-items: center;
    justify-content: center;
    font-weight: 700;
    text-transform: uppercase;
  }
  .band--title {
    top: 66px;
    height: 68px;
    font-size: 50px;
    letter-spacing: 0.5px;
  }
  .band--caption {
    top: 666px;
    height: 68px;
    font-size: 26px;
    word-spacing: 6px;
    letter-spacing: 1px;
  }
  .factors {
    position: absolute;
    left: 0;
    top: 0;
    width: 1200px;
    height: 800px;
  }
  .halo { fill: var(--halo); opacity: 0.85; }
  .ring { fill: var(--ring); }
  .core { fill: var(--navy); }
  .ring-label {
    fill: var(--white);
    font-weight: 600;
    font-size: 14px;
    letter-spacing: 1px;
  }
  .factor-list {
    fill: var(--white);
    font-size: 15.5px;
    font-weight: 400;
  }
  .arrow { fill: var(--halo); }
</style>
</head>
<body>
<main class="canvas">
  <header class="band band--title">Equity, Effectiveness, Efficiency</header>

  <svg class="factors" viewBox="0 0 1200 800" xmlns="http://www.w3.org/2000/svg">
    <defs>
      <path id="ring-path-supply" d="M46,400 a154,154 0 1,1 308,0 a154,154 0 1,1 -308,0"/>
      <path id="ring-path-capacity" d="M446,400 a154,154 0 1,1 308,0 a154,154 0 1,1 -308,0"/>
      <path id="ring-path-demand" d="M846,400 a154,154 0 1,1 308,0 a154,154 0 1,1 -308,0"/>
      <polygon id="arrow-down" points="-11,0 11,0 11,20 22,20 0,43 -22,20 -11,20"/>
      <polygon id="arrow-up" points="-11,43 11,43 11,23 22,23 0,0 -22,23 -11,23"/>
    </defs>

    <!-- arrows -->
    <g class="arrow">
      <use href="#arrow-down" x="200" y="145"/>
      <use href="#arrow-down" x="600" y="145"/>
      <use href="#arrow-down" x="1000" y="145"/>
      <use href="#arrow-up" x="200" y="612"/>
      <use href="#arrow-up" x="600" y="612"/>
      <use href="#arrow-up" x="1000" y="612"/>
    </g>

    <!-- supply -->
    <g class="factor factor--supply">
      <circle class="halo" cx="200" cy="400" r="198" role="img" aria-label="Distressed ink texture around the supply circle"/>
      <circle class="ring" cx="200" cy="400" r="173"/>
      <circle class="core" cx="200" cy="400" r="147"/>
      <text class="ring-label"><textPath href="#ring-path-supply" textLength="955" lengthAdjust="spacing">SUPPLY SUPPLY SUPPLY SUPPLY SUPPLY SUPPLY SUPPLY SUPPLY SUPPLY SUPPLY SUPPLY SUPPLY SUPPLY</textPath></text>
      <text class="factor-list" x="98" y="361">
        <tspan x="98" dy="0">1.Uncertain material supply</tspan>
        <tspan x="98" dy="17.6">2.Uncertain monetary supply</tspan>
        <tspan x="98" dy="17.6">3.Limited food supply</tspan>
        <tspan x="98" dy="17.6">4.Perishability</tspan>
        <tspan x="98" dy="17.6">5.Donor constraints</tspan>
        <tspan x="98" dy="17.6">6.Donor relationships</tspan>
      </text>
    </g>

    <!-- capacity -->
    <g class="factor factor--capacity">
      <circle class="halo" cx="600" cy="400" r="198" role="img" aria-label="Distressed ink texture around the capacity circle"/>
      <circle class="ring" cx="600" cy="400" r="173"/>
      <circle class="core" cx="600" cy="400" r="147"/>
      <text class="ring-label"><textPath href="#ring-path-capacity" textLength="955" lengthAdjust="spacing">CAPACITY CAPACITY CAPACITY CAPACITY CAPACITY CAPACITY CAPACITY CAPACITY CAPACITY CAPACITY CAPACITY</textPath></text>
      <text class="factor-list" x="513" y="307">
        <tspan x="513" dy="0">11.Storage</tspan>
        <tspan x="531" dy="17.6">a)Cold</tspan>
        <tspan x="531" dy="17.6">b)Warehouse</tspan>
        <tspan x="513" dy="17.6">12.Transportation</tspan>
        <tspan x="513" dy="17.6">13.Workforce</tspan>
        <tspan x="531" dy="17.6">a)Volunteers</tspan>
        <tspan x="531" dy="17.6">b)Expertise &amp; training</tspan>
        <tspan x="531" dy="17.6">c)Attitudes &amp; Beliefs</tspan>
        <tspan x="531" dy="17.6">d)Collaboration</tspan>
        <tspan x="531" dy="17.6">e)Executive Support</tspan>
        <tspan x="513" dy="17.6">14.External stakeholders</tspan>
        <tspan x="513" dy="17.6">15.Budget</tspan>
      </text>
    </g>

    <!-- demand -->
    <g class="factor factor--demand">
      <circle class="halo" cx="1000" cy="400" r="198" role="img" aria-label="Distressed ink texture around the demand circle"/>
      <circle class="ring" cx="1000" cy="400" r="173"/>
      <circle class="core" cx="1000" cy="400" r="147"/>
      <text class="ring-label"><textPath href="#ring-path-demand" textLength="955" lengthAdjust="spacing">DEMAND DEMAND DEMAND DEMAND DEMAND DEMAND DEMAND DEMAND DEMAND DEMAND DEMAND DEMAND</textPath></text>
      <text class="factor-list" x="904" y="378">
        <tspan x="904" dy="0">7.Uncertain demand</tspan>
        <tspan x="904" dy="17.6">8.Limited demand visibility</tspan>
        <tspan x="904" dy="17.6">9.Client choice</tspan>
        <tspan x="904" dy="17.6">10.Food wastage</tspan>
      </text>
    </g>
  </svg>

  <footer class="band band--caption">Factors that affect the introduction of nutrition’s policy</footer>
</main>
</body>
</html>
```